Movie Poster Design Needed for Psychological Horror Short Film

Our new animated psychological horror short film The Quiet Hollow needs a poster that will capture peoples attention at film festivals and online. We have provided screenshots from the movie but designs are not limited to using those. We want to convey something personally unsettling and potentially evil, but this isnt a slasher or outright horror film: the horror takes place in a young girls mind and what she chooses to do about The Quiet Hollow.

Target Market(s)

Adults over the age of 18.

Industry/Entity Type

Movie Production

Font styles to use
Sans Serif

Colors

Designer to choose colors to be used in the design.

Requirements
Must have
• Must be vertical design. Must include these phrases on the poster:
• Written by Tom Verlasky
• Lantern Moth Productions
Nice to have
• Clean modern look
Should not have
• Over-the-top fonts

```html
<!DOCTYPE html>
<html lang="en">
<head>
<meta charset="utf-8">
<title>The Quiet Hollow — Poster</title>
<link rel="stylesheet" href="https://fonts.googleapis.com/css2?family=Bebas+Neue&family=Montserrat:wght@300&display=swap">
<style>
  :root {
    --night: #191919;
    --ground: #131313;
    --blood-deep: #3a1416;
    --blood: #6e1214;
    --title-white: #f7f7f7;
    --title-red: #c8161b;
    --credit-white: #ffffff;
  }
  html, body {
    margin: 0;
    padding: 0;
    overflow: hidden;
    background: var(--ground);
  }
  .poster {
    position: relative;
    width: 848px;
    height: 1200px;
    overflow: hidden;
    background: var(--ground);
  }
  .poster__scene {
    position: absolute;
    left: 0;
    top: 0;
    width: 848px;
    height: 815px;
    background: linear-gradient(
      to bottom,
      var(--night) 0%,
      var(--night) 30%,
      var(--blood-deep) 58%,
      var(--blood) 100%
    );
    border-bottom-left-radius: 50% 18px;
    border-bottom-right-radius: 50% 18px;
  }
  .poster__title {
    position: absolute;
    left: 0;
    top: 0;
    width: 848px;
    height: 1000px;
    margin: 0;
    font-family: "Bebas Neue", "Oswald", sans-serif;
    font-weight: 400;
    line-height: 1;
  }
  .poster__title-line {
    display: block;
    position: absolute;
    left: 0;
    width: 848px;
    text-align: center;
    white-space: nowrap;
  }
  .poster__title-line--top {
    top: 305px;
    font-size: 290px;
    color: var(--title-white);
    letter-spacing: 6px;
  }
  .poster__title-line--middle {
    top: 560px;
    font-size: 250px;
    color: var(--title-white);
    letter-spacing: 4px;
  }
  .poster__title-line--bottom {
    top: 828px;
    font-size: 140px;
    color: var(--title-red);
    letter-spacing: 6px;
  }
  .poster__credits {
    position: absolute;
    left: 0;
    top: 1094px;
    width: 848px;
    text-align: center;
    font-family: "Montserrat", sans-serif;
    font-weight: 300;
    color: var(--credit-white);
    text-transform: uppercase;
  }
  .poster__studio,
  .poster__writer {
    margin: 0;
    font-size: 28px;
    line-height: 1;
    letter-spacing: 0.5px;
    white-space: nowrap;
  }
  .poster__writer {
    margin-top: 30px;
  }
</style>
</head>
<body>
  <main class="poster">
    <div class="poster__scene" role="img" aria-label="Glowing red eyes staring from a dark sky above bare twisted trees, a crooked iron fence and a black hillside under a blood-red horizon"></div>

    <h1 class="poster__title">
      <span class="poster__title-line poster__title-line--top">The</span>
      <span class="poster__title-line poster__title-line--middle">Quiet</span>
      <span class="poster__title-line poster__title-line--bottom">Hollow</span>
    </h1>

    <footer class="poster__credits">
      <p class="poster__studio">Lantern Moth Productions</p>
      <p class="poster__writer">Written by Tom Verlasky</p>
    </footer>
  </main>
</body>
</html>
```